Plumweave Inc. Website & Korvix Apps Landing Pages

We need a web site design for our company. We develop software and do various consultant projects for our clients. Our products focus on the mobile platform, mainly the Korvix (business, games, social, etc.). We want to communicate that our software is simple and good as candy. The web pages should be fun to look at not loosing seriousness and credibility. Web 2.0 style and 960 grid system a must. We are opened to any overall site colour scheme suggestions (look at the sites we like below).

Must haves:
- Our logo should be seen on the site and look great on it :-) (preview attached below)
- Main home page and app landing page.
- Section links/tabs on the home page (home,apps,support,blog,contact,about)
- No text in images
- Style sheet

Looks we like:
- http://x7k3lmq9pwrtzv.pixelmoorvault.net/412_Zelto_Site/final_large.jpg
- http://x7k3lmq9pwrtzv.pixelmoorvault.net/Premium_71_Illustrative_Korvix_Landing_Page/final.jpg
- http://grelmwick.com/
- http://dorniply.ca/
- http://quatzel.com/

Industry/Entity Type

Business

Requirements
Must have
• - Company logo should look great on pages.
• - Main home page and app landing page.
• - Section links/tabs on the home page (home,apps,support,blog,contact,about)
• - Web 2.0 style.
• - 960 grid system (12 col, 16 col).
• - Sliced ann optmized
• - Exported in all major formats (psd,ai,eps,png,jpeg,etc)
• - Style sheet
Should not have
• - Text in images

```html
<!DOCTYPE html>
<html lang="en">
<head>
<meta charset="utf-8">
<title>Plumweave</title>
<link rel="stylesheet" href="https://fonts.googleapis.com/css2?family=Arimo:wght@400;700&family=Open+Sans:wght@400;600;700&display=swap">
<style>
:root{
  --page:#d4d4d4;
  --panel:#ffffff;
  --ink:#444444;
  --muted:#6b6b6b;
  --red:#d0211e;
  --red-dark:#5a0505;
  --orange:#f08a12;
  --orange-light:#ffb533;
  --footer:#333333;
  --footer-text:#d6d6d6;
  --bar:#151515;
}
*{box-sizing:border-box;margin:0;padding:0}
html,body{width:831px;height:1200px;overflow:hidden}
body{background:linear-gradient(var(--page) 0,var(--page) 900px,var(--footer) 900px);font-family:"Arimo",Arial,sans-serif;color:var(--ink);position:relative}
.site-panel{position:absolute;left:33px;top:0;width:770px;height:922px;background:var(--panel);border-radius:0 0 8px 8px;box-shadow:0 2px 8px rgba(0,0,0,.35)}
.brand{position:absolute;left:22px;top:30px;display:flex;align-items:center;gap:10px;font-family:"Open Sans",sans-serif;font-weight:700;font-size:34px;color:#333;white-space:nowrap}
.brand-dot{width:20px;height:20px;border-radius:50%;background:var(--red)}
.main-nav{position:absolute;right:14px;top:14px;display:flex;gap:6px}
.main-nav a{display:flex;flex-direction:column;align-items:center;width:58px;text-decoration:none;color:#555;font-size:15px;font-weight:700;font-family:"Open Sans",sans-serif;white-space:nowrap}
.main-nav .icon{width:30px;height:30px;margin-bottom:4px}
.main-nav a.active{color:var(--red);border-bottom:3px solid var(--red);padding-bottom:2px}
.hero{position:absolute;left:17px;top:111px;width:736px;height:360px;border-radius:4px;overflow:hidden;background:radial-gradient(ellipse at 30% 40%,#e8322a 0%,#a80e0c 45%,var(--red-dark) 100%)}
.hero-art{position:absolute;left:110px;top:10px;width:430px;height:340px;background:linear-gradient(160deg,#2a2a2a,#0d0d0d);border-radius:30px;opacity:.85}
.download{position:absolute;right:18px;bottom:16px;width:236px;height:55px;border-radius:6px;background:linear-gradient(var(--orange-light),var(--orange));display:flex;align-items:center;justify-content:center;gap:10px;font-family:"Open Sans",sans-serif;font-weight:700;font-size:20px;color:#3a1d00;white-space:nowrap;box-shadow:0 2px 4px rgba(0,0,0,.4)}
.download svg{flex:none}
.columns{position:absolute;left:17px;top:512px;width:736px;display:flex;gap:20px}
.col{flex:1;min-width:0}
.col h2{display:flex;align-items:center;gap:8px;font-family:"Open Sans",sans-serif;font-weight:600;font-size:19px;color:var(--red);white-space:nowrap;height:40px;border-bottom:1px solid #ddd;margin-bottom:14px}
.col h2 svg{flex:none;width:28px;height:28px}
.features li{list-style:none;display:flex;gap:8px;font-size:12.5px;line-height:16px;color:var(--muted);margin-bottom:14px}
.features svg{flex:none;width:14px;height:14px;margin-top:2px}
.demo{height:240px;background:#111;border-radius:4px;position:relative;border:4px solid #ddd}
.demo-play{position:absolute;left:50%;top:44%;transform:translate(-50%,-50%);width:60px;height:22px;border-radius:4px;background:#555}
.demo-bar{position:absolute;left:0;right:0;bottom:0;height:18px;background:#2b2b2b}
.quote{font-size:12.5px;line-height:17px;color:var(--muted)}
.quote strong{display:block;color:#222;margin-top:4px}
.site-footer{position:absolute;left:33px;top:936px;width:770px;height:168px;display:flex;gap:30px;padding:0 5px;overflow:hidden}
.site-footer section{flex:1;min-width:0}
.site-footer h3{font-size:16px;color:#fff;margin:10px 0 8px;font-weight:700}
.site-footer p{font-size:11px;line-height:14px;color:var(--footer-text);margin-bottom:6px}
.bottom-bar{position:absolute;left:0;top:1108px;width:831px;height:92px;background:var(--bar);display:flex;align-items:center;justify-content:space-between;padding:0 40px}
.bottom-nav{font-size:12px;font-weight:700;color:#fff;white-space:nowrap}
.bottom-nav span{margin:0 5px;color:#999}
.bottom-brand{text-align:right;color:#fff;font-family:"Open Sans",sans-serif;font-weight:700;font-size:24px;white-space:nowrap}
.bottom-brand small{display:block;font-size:9px;font-weight:400;color:#888}
</style>
</head>
<body>
<div class="site-panel">
  <div class="brand"><span class="brand-dot"></span>Plumweave</div>
  <nav class="main-nav">
    <a class="active" href="#"><svg class="icon" viewBox="0 0 30 30"><path d="M3 15 15 4l12 11h-4v11h-6v-7h-4v7H7V15z" fill="#1f8fd0"/></svg>home</a>
    <a href="#"><svg class="icon" viewBox="0 0 30 30"><rect x="5" y="5" width="20" height="20" rx="5" fill="#39a82f"/></svg>apps</a>
    <a href="#"><svg class="icon" viewBox="0 0 30 30"><circle cx="15" cy="15" r="11" fill="#e23b2e"/><circle cx="15" cy="15" r="5" fill="#fff"/></svg>support</a>
    <a href="#"><svg class="icon" viewBox="0 0 30 30"><rect x="4" y="4" width="22" height="22" rx="4" fill="#f59a1e"/><circle cx="10" cy="20" r="2.5" fill="#fff"/></svg>blog</a>
    <a href="#"><svg class="icon" viewBox="0 0 30 30"><rect x="3" y="7" width="24" height="16" rx="2" fill="#1f8fd0"/><path d="M3 8l12 9 12-9" stroke="#fff" stroke-width="2" fill="none"/></svg>contact</a>
    <a href="#"><svg class="icon" viewBox="0 0 30 30"><circle cx="15" cy="10" r="5" fill="#39a82f"/><path d="M5 27c0-7 4-10 10-10s10 3 10 10z" fill="#39a82f"/></svg>about</a>
  </nav>
  <div class="hero">
    <div class="hero-art" role="img" aria-label="Two Korvix phones showing app screens"></div>
    <div class="download">DOWNLOAD NOW
      <svg width="26" height="26" viewBox="0 0 26 26"><circle cx="13" cy="13" r="12" fill="#c0392b"/><path d="M13 6v11M8 12l5 5 5-5" stroke="#fff" stroke-width="3" fill="none"/></svg>
    </div>
  </div>
  <div class="columns">
    <section class="col">
      <h2><svg viewBox="0 0 30 30"><rect x="4" y="6" width="20" height="20" fill="#7aa7d8"/><path d="M8 12h12M8 17h12M8 22h8" stroke="#fff" stroke-width="2"/></svg>Features</h2>
      <ul class="features">
        <li><svg viewBox="0 0 14 14"><path d="M1 7l4 4 8-9" stroke="#555" stroke-width="2" fill="none"/></svg>Lorem ipsum dolor sit amet, consectetur adipiscing elit. Nam eget magna non.</li>
        <li><svg viewBox="0 0 14 14"><path d="M1 7l4 4 8-9" stroke="#555" stroke-width="2" fill="none"/></svg>Lorem ipsum dolor sit amet, consectetur adipiscing elit. Nam eget magna non.</li>
        <li><svg viewBox="0 0 14 14"><path d="M1 7l4 4 8-9" stroke="#555" stroke-width="2" fill="none"/></svg>Lorem ipsum dolor sit amet, consectetur adipiscing elit. Nam eget magna non.</li>
        <li><svg viewBox="0 0 14 14"><path d="M1 7l4 4 8-9" stroke="#555" stroke-width="2" fill="none"/></svg>Lorem ipsum dolor sit amet, consectetur adipiscing elit. Nam eget magna non.</li>
      </ul>
    </section>
    <section class="col">
      <h2><svg viewBox="0 0 30 30"><circle cx="10" cy="10" r="5" fill="#f59a1e"/><rect x="14" y="8" width="14" height="12" fill="#1f8fd0"/><path d="M2 28c0-8 4-11 8-11s8 3 8 11z" fill="#f59a1e"/></svg>Check out the DEMO</h2>
      <div class="demo" role="img" aria-label="Demo video player">
        <div class="demo-play"></div>
        <div class="demo-bar"></div>
      </div>
    </section>
    <section class="col">
      <h2><svg viewBox="0 0 30 30"><circle cx="10" cy="10" r="5" fill="#1f8fd0"/><circle cx="20" cy="12" r="5" fill="#39a82f"/><path d="M2 28c0-8 4-11 8-11s8 3 8 11z" fill="#1f8fd0"/></svg>Testimonials</h2>
      <p class="quote">"We had been waiting for an easy to use application like Plumweave that would combine collaboration functions (similar to those in popular social networking sites), security that would enable us to protect assets and access, and robust file sharing that was reliable and would accommodate the size and variety of files we work with."
        <strong>Marlo Fenwick<br>CEO, Company</strong></p>
    </section>
  </div>
</div>

<footer class="site-footer">
  <section>
    <h3>About Plumweave</h3>
    <p>Lorem ipsum dolor sit amet, consectetur adipiscing elit. Nam eget magna non. Lorem ipsum dolor sit amet, consectetur adipiscing elit. Nam eget magna non.</p>
    <p>Lorem ipsum dolor sit amet, consectetur adipiscing elit. Nam eget magna non.</p>
  </section>
  <section>
    <h3>Support</h3>
    <p>Lorem ipsum dolor sit amet, consectetur adipiscing elit. Nam eget magna non. Lorem ipsum dolor sit amet, consectetur adipiscing elit. Nam eget magna non. Lorem ipsum dolor sit amet, consectetur adipiscing elit.</p>
  </section>
  <section>
    <h3>Our Blog</h3>
    <p>Lorem ipsum dolor sit amet, consectetur<br>Oct 25, 2010</p>
    <p>Lorem ipsum dolor sit amet, consectetur<br>Oct 26, 2010</p>
    <p>Lorem ipsum dolor sit amet, consectetur<br>Oct 29, 2010</p>
  </section>
</footer>

<div class="bottom-bar">
  <div class="bottom-nav">home<span>/</span>apps<span>/</span>support<span>/</span>blog<span>/</span>contact<span>/</span>about</div>
  <div class="bottom-brand">Plumweave<small>Copyright 2010. All rights reserved.</small></div>
</div>
</body>
</html>
```